Goodnight sleep Collagen milk drink

We need a modern attractive package design for carton . with sachet inside . This is a collagen milk powder targeting young women . 16 - 40 . it contains marine collagen , skim milk powder and other ingredients designed for maintain healthy skin while sleeping. To drink before sleep. the size is 18 cm h x 8.5 cm w x 6.2 cm D , with a slot can tear off on bottom so the sachet can take out .
Updates

Target Market(s)

women , 16 - 40 ,

Industry/Entity Type

Health Care

Colors
0492cd
3176b5
eea4c8
0255a3
6b449b
a54499

Requirements
Must have
• product name : VelvaDorm , clean modern for young women
Nice to have
• represent the idea of beauty , goodnight sleep , elements for ingredients marine collagen , lemon balm , passion flower .

```html
<!DOCTYPE html>
<html lang="en">
<head>
<meta charset="utf-8">
<title>VelvaDorm Marine Collagen Skim Milk Powder – Carton and Sachet</title>
<link href="https://fonts.googleapis.com/css2?family=Kaushan+Script&family=Courgette&family=Oswald:wght@500;600&display=swap" rel="stylesheet">
<style>
  :root{
    --stage:#e9e9eb;
    --sky-top:#4d92d6;
    --sky-mid:#a9d2f0;
    --meadow:#c9e07a;
    --brand-pink:#e0147f;
    --navy:#1e2a6a;
    --badge:#27407e;
    --white:#ffffff;
    --milk:#f4f6fa;
    --milk-shade:#c9d3e2;
  }
  *{box-sizing:border-box;margin:0;padding:0}
  html,body{width:1200px;height:801px;overflow:hidden;background:var(--stage)}
  .stage{position:relative;width:1200px;height:801px}

  .panel{
    position:absolute;overflow:hidden;
    background:linear-gradient(180deg,var(--sky-top) 0%,var(--sky-mid) 55%,var(--meadow) 100%);
    box-shadow:0 18px 40px rgba(40,50,70,.18);
  }
  .carton-front{left:330px;top:80px;width:304px;height:644px}
  .sachet{left:720px;top:200px;width:250px;height:340px;border-radius:4px}
  .sachet::before,.sachet::after{
    content:"";position:absolute;left:0;right:0;height:14px;
    background:repeating-linear-gradient(90deg,rgba(255,255,255,.25) 0 2px,transparent 2px 5px);
  }
  .sachet::before{top:0}
  .sachet::after{bottom:0}

  .brand{
    position:absolute;left:0;right:0;text-align:center;
    font-family:"Kaushan Script",cursive;color:var(--brand-pink);
  }
  .descriptor{
    position:absolute;left:0;right:0;text-align:center;
    font-family:"Courgette",cursive;color:var(--navy);line-height:1.2;
  }
  .carton-front .brand{top:36px;font-size:50px}
  .carton-front .descriptor{top:112px;font-size:24px}
  .sachet .brand{top:26px;font-size:36px}
  .sachet .descriptor{top:80px;font-size:16px}

  .splash-art{
    position:absolute;
    background:radial-gradient(ellipse at 50% 45%,var(--milk) 0%,var(--milk) 38%,var(--milk-shade) 62%,rgba(255,255,255,0) 72%);
  }
  .carton-front .splash-art{left:22px;top:210px;width:260px;height:360px}
  .sachet .splash-art{left:30px;top:128px;width:190px;height:190px}

  .duration-badge{
    position:absolute;background:var(--badge);color:var(--white);
    border-radius:14px;text-align:center;font-family:"Oswald",sans-serif;
  }
  .duration-badge .days{display:block;font-weight:600;letter-spacing:.5px}
  .duration-badge .tagline{display:block;font-weight:500;text-transform:uppercase;opacity:.85}
  .carton-front .duration-badge{left:18px;bottom:22px;padding:4px 14px 6px}
  .carton-front .days{font-size:20px;line-height:1.1}
  .carton-front .tagline{font-size:7px;letter-spacing:.6px}
  .sachet .duration-badge{left:12px;bottom:22px;padding:2px 9px 4px;border-radius:10px}
  .sachet .days{font-size:13px;line-height:1.1}
  .sachet .tagline{font-size:5px;letter-spacing:.4px}
</style>
</head>
<body>
<main class="stage">
  <section class="panel carton-front" aria-label="Carton front panel">
    <h1 class="brand">VelvaDorm</h1>
    <p class="descriptor">Marine Collagen<br>Skim Milk Powder</p>
    <div class="splash-art" role="img" aria-label="Milk splash swirling around a glass"></div>
    <div class="duration-badge"><span class="days">30 DAYS</span><span class="tagline">Night Beauty Drink</span></div>
  </section>

  <section class="panel sachet" aria-label="Sachet">
    <h2 class="brand">VelvaDorm</h2>
    <p class="descriptor">Marine Collagen<br>Skim Milk Powder</p>
    <div class="splash-art" role="img" aria-label="Milk pouring into a glass with splash"></div>
    <div class="duration-badge"><span class="days">30 DAYS</span><span class="tagline">Night Beauty Drink</span></div>
  </section>
</main>
</body>
</html>
```